I want a business letter head designed, one that I can have printed but also one that I can use as an insert for proforma documentation that is printed in house.

Business name : RJ Penfold & Associates
Address: PO Box 738
Tewantin Qld 4587

Type of business: Accounting practice- accounting, taxation, audit, self managed superannuation,

Colour scheme: black and blue - previously designed a business card; however the blue that is one the cards is very washed out and I am not particularly happy with it.

Industry/Entity Type

Business

```html
<!DOCTYPE html>
<html lang="en">
<head>
<meta charset="utf-8">
<title>RJ Penfold &amp; Associates — Letterhead</title>
<link rel="stylesheet" href="https://fonts.googleapis.com/css2?family=Alfa+Slab+One&family=Graduate&display=swap">
<style>
  :root {
    --paper: #ffffff;
    --brand-blue: #2893bb;
    --brand-black: #000000;
    --ink-light: #ffffff;
  }
  html, body {
    margin: 0;
    padding: 0;
    overflow: hidden;
    background: var(--paper);
  }
  .letterhead {
    position: relative;
    width: 927px;
    height: 1200px;
    overflow: hidden;
    background: var(--paper);
  }
  .letterhead__art {
    position: absolute;
    inset: 0;
    display: block;
  }
  .accent-band { fill: var(--brand-blue); }
  .footer-band { fill: var(--brand-black); }
  .company-name-vertical {
    font-family: "Graduate", "Alfa Slab One", serif;
    font-size: 46px;
    fill: var(--ink-light);
  }
  .postal-address {
    font-family: "Alfa Slab One", serif;
    font-size: 30px;
    fill: var(--ink-light);
  }
  .brand-mark-square { fill: var(--brand-blue); }
  .brand-mark-name {
    font-family: "Alfa Slab One", serif;
    font-size: 28px;
    fill: var(--ink-light);
  }
</style>
</head>
<body>
  <main class="letterhead">
    <svg class="letterhead__art" width="927" height="1200" viewBox="0 0 927 1200" xmlns="http://www.w3.org/2000/svg">
      <polygon class="accent-band" points="756,0 927,0 927,1013 717,1000"/>
      <polygon class="footer-band" points="0,944 927,1013 927,1200 0,1200"/>

      <text class="company-name-vertical" transform="translate(800,93) rotate(90)"
            textLength="887" lengthAdjust="spacingAndGlyphs">RJ Penfold &amp; Associates</text>

      <text class="postal-address" x="84" y="1070">PO Box 738</text>
      <text class="postal-address" x="84" y="1111">Tewantin Qld 4587</text>

      <rect class="brand-mark-square" x="572" y="1040" width="52" height="52"/>
      <text class="brand-mark-name" x="640" y="1062">RJ Penfold</text>
      <text class="brand-mark-name" x="640" y="1098">&amp; Associates</text>
    </svg>
  </main>
</body>
</html>
```